Premium Coffee Business Needs a Wordpress Design

We need a Wordpress design for a Premium Coffee E-commerce based in Sao Paulo, Brazil. We want something very similar to tallowfinchroasters.com, but with a few exceptions, better described in the attachment (PLEASE READ our specifications). The product we're selling is premium, so we need to communicate sophistication, and at the same time people should feel they're in contact with an innovative company. Our company is called Coffee Meridian.
Adults aged 25 to 50 who have refined tastes.
Business

```html
<!DOCTYPE html>
<html lang="en">
<head>
<meta charset="utf-8">
<title>Meridian Premium Coffee</title>
<link href="https://fonts.googleapis.com/css2?family=Quicksand:wght@400;500;600;700&display=swap" rel="stylesheet">
<style>
  :root{
    --orange:#d98a2e;
    --orange-deep:#b8601a;
    --accent:#dd7f22;
    --brown:#4a3426;
    --brown-dark:#3b281a;
    --text-muted:#8a7a6c;
    --cream:#fbf4e6;
    --white:#ffffff;
  }
  *{box-sizing:border-box;margin:0;padding:0}
  html,body{width:1074px;height:1200px;overflow:hidden;background:var(--white)}
  body{font-family:"Quicksand",sans-serif;color:var(--brown)}
  .page{position:relative;width:1074px;height:1200px;overflow:hidden}

  .site-header{position:absolute;left:0;top:0;width:1074px;height:89px;
    background:linear-gradient(180deg,#d88a35 0%,#b65f1c 100%)}
  .brand{position:absolute;left:107px;top:28px;font-size:22px;font-weight:700;color:var(--white)}
  .main-nav{position:absolute;left:389px;top:36px;display:flex;gap:25px;font-size:14px;font-weight:600;color:var(--white)}
  .cart{position:absolute;left:932px;top:33px}

  .hero{position:absolute;left:0;top:89px;width:1074px;height:426px;
    background:linear-gradient(90deg,#fbf0d6 0%,#f6e6c3 45%,#efe0c4 60%,#e8d6b6 100%)}
  .hero-photo{position:absolute;left:460px;top:0;width:614px;height:426px;
    background:radial-gradient(ellipse at 55% 45%,#6b4a33 0%,#a8805d 18%,#efe8df 32%,#f4ecdc 55%,rgba(246,230,195,0) 75%)}
  .hero-copy{position:absolute;left:101px;top:218px}
  .hero-title{font-size:32px;font-weight:700;color:var(--brown);letter-spacing:.3px;line-height:1.1}
  .hero-sub{font-size:23px;font-weight:700;color:var(--accent);margin-top:5px}
  .hero-text{font-size:12px;line-height:21px;color:var(--brown);margin-top:10px;width:330px}
  .dots{display:flex;gap:5px;margin-top:14px}
  .dots span{width:11px;height:11px;border-radius:50%;background:#cfc3b4}
  .dots span.active{background:var(--brown)}

  .intro{position:absolute;left:0;top:560px;width:1074px;text-align:center}
  .intro h2{font-size:28px;font-weight:500;color:var(--brown)}
  .intro h3{font-size:17px;font-weight:500;color:var(--accent);margin-top:8px}
  .intro p{font-size:11.5px;line-height:19px;color:var(--text-muted);width:740px;margin:12px auto 0}

  .feature{position:absolute;top:712px;width:200px;text-align:center}
  .feature-art{width:90px;height:108px;margin:0 auto;border-radius:8px}
  .feature h4{font-size:18px;font-weight:500;color:var(--accent);margin-top:22px;line-height:22px}
  .feature p{font-size:11px;line-height:18px;color:var(--text-muted);margin-top:6px}
  .btn-outline{position:absolute;top:221px;left:45px;width:110px;height:29px;border:2px solid var(--accent);
    color:var(--accent);font-size:11px;font-weight:700;line-height:25px;text-align:center}

  .footer-links{position:absolute;left:0;top:1057px;width:1074px;height:61px;background:var(--cream)}
  .footer-links nav{position:absolute;left:118px;top:20px;display:flex;gap:37px;font-size:14px;font-weight:500;color:var(--brown)}
  .social{position:absolute;left:840px;top:19px;display:flex;gap:3px}
  .social span{width:22px;height:22px;border-radius:50%;background:var(--accent)}

  .footer-bottom{position:absolute;left:0;top:1118px;width:1074px;height:82px;background:var(--brown-dark)}
  .email{position:absolute;left:125px;top:29px;width:258px;height:28px;border:1px solid #6b5544;background:#4b3526;
    color:#d8cbbd;font-size:11px;line-height:26px;padding-left:12px}
  .signup{position:absolute;left:395px;top:29px;width:72px;height:28px;background:var(--orange);color:var(--white);
    font-size:13px;font-weight:600;text-align:center;line-height:28px}
  .legal{position:absolute;right:113px;top:30px;font-size:11.5px;color:#d8cbbd}
</style>
</head>
<body>
<div class="page">
  <header class="site-header">
    <div class="brand">Meridian Premium Coffee</div>
    <nav class="main-nav">
      <span>Home</span><span>Brewing Guides</span><span>Subscriptions</span><span>Merchandise</span><span>Blog</span><span>Our Story</span>
    </nav>
    <svg class="cart" width="22" height="22" viewBox="0 0 22 22" aria-label="Cart">
      <path d="M1 3h4l3 11h10l3-8H7" fill="none" stroke="#fff" stroke-width="2.4" stroke-linejoin="round"/>
      <rect x="7" y="6" width="13" height="7" fill="#fff"/>
      <circle cx="9" cy="18.5" r="2" fill="#fff"/><circle cx="17" cy="18.5" r="2" fill="#fff"/>
    </svg>
  </header>

  <section class="hero">
    <div class="hero-photo" role="img" aria-label="Cup of coffee on a saucer with milk being poured in"></div>
    <div class="hero-copy">
      <div class="hero-title">VIVAMUS PORTTITOR PURUS</div>
      <div class="hero-sub">MAURIS VEL LACUS VITAE FELIS</div>
      <p class="hero-text">Etiam est nunc venenatis in tristique eu imperdiet ac nisl Cum sociis natoque penatibus et magnis dis parturient</p>
      <div class="dots"><span class="active"></span><span></span><span></span><span></span></div>
    </div>
  </section>

  <section class="intro">
    <h2>Donec scelerisque leo ac risus Praesent sit</h2>
    <h3>Etiam est nunc venenatis in tristique eu imperdiet</h3>
    <p>Mauris vel lacus vitae felis vestibulum volutpat Etiam est nunc venenatis in tristique eu imperdiet ac nisl Cum sociis natoque penatibus et magnis dis parturient montes nascetur ridiculus mus In iaculis facilisis massa Etiam eu urna Sed porta</p>
  </section>

  <article class="feature" style="left:103px">
    <div class="feature-art" role="img" aria-label="Green coffee seedling" style="background:linear-gradient(160deg,#9bd64a,#4f9a1e)"></div>
    <h4>Coffee Plant</h4>
    <p>Mauris vel lacus vitae felis vestibulum volutpat Etiam est nunc venenatis in tristique eu imperdiet ac nisl</p>
    <div class="btn-outline">LEARN MORE</div>
  </article>
  <article class="feature" style="left:324px">
    <div class="feature-art" role="img" aria-label="Espresso roasting machine" style="background:linear-gradient(160deg,#d8d8d8,#7c7c7c)"></div>
    <h4>Coffee Roasting<br>Machine</h4>
    <p>Mauris vel lacus vitae felis vestibulum volutpat Etiam est nunc venena</p>
    <div class="btn-outline">LEARN MORE</div>
  </article>
  <article class="feature" style="left:543px">
    <div class="feature-art" role="img" aria-label="Hand truck carrying shipping boxes" style="background:linear-gradient(160deg,#f07a4a,#c8452a)"></div>
    <h4>Shipping Process</h4>
    <p>Mauris vel lacus vitae felis vestibulum volutpat Etiam est nunc venenatis in tristique eu imperdiet ac nisl</p>
    <div class="btn-outline">LEARN MORE</div>
  </article>
  <article class="feature" style="left:767px">
    <div class="feature-art" role="img" aria-label="Steaming red and gold coffee cup" style="background:linear-gradient(160deg,#f2b640,#b8271c)"></div>
    <h4>Cup of Coffee</h4>
    <p>Mauris vel lacus vitae felis vestibulum volutpat Etiam est nunc venenatis in tristique eu imperdiet ac nisl</p>
    <div class="btn-outline">LEARN MORE</div>
  </article>

  <footer>
    <div class="footer-links">
      <nav><span>Contact</span><span>Special Orders</span><span>Wholesale</span><span>Press</span><span>FAQ</span></nav>
      <div class="social" aria-label="Social links"><span></span><span></span><span></span><span></span></div>
    </div>
    <div class="footer-bottom">
      <div class="email">Enter email address</div>
      <div class="signup">Sign Up</div>
      <div class="legal">Terms of Use &nbsp;/&nbsp; Privacy &nbsp;&nbsp;© 2014 Company Name. All right reserved</div>
    </div>
  </footer>
</div>
</body>
</html>
```